earthmoving and roadworks company looking for a fresh and updated logo to help us stand out

We are looking for a business card design for our earthmoving, demolition and road works company named Wandermere Plant. We cover a broad range of work so our business card needs to be flexible to suit all of the different services we provide. We have a few different bits of machinery including several water trucks for transporting water and spraying the roads, an excavator (digger) for earthmoving, a tipper truck that carries grain/soil and other items, a bobcat and two rollers. our business card needs to be simple but effective and bold. Our colour palette is yellow, black and white and I have attached a copy of our logo but please note our logo is only the 'Wandermere plant' bit with attached circle, the 'watercarts, rollers, cartage' below are not part of the logo. Please feel free to modify the logo to better suit the business card. The design must be easy to read and to the point. It should make us look reliable and professional.

Target Market(s)

Wide range of clients including government sectors and private individuals

Industry/Entity Type

Construction

Contact Information for Business Card

We need a business card that is bold and straight to the point but with easy to read information and an eye catching design. We are open to either a single sided or double sided design

Colors
fbee3d
fcf5b5
fbf289
fbed22

Requirements
Must have
• The business card must include
• our logo
• our contact details as listed below:
• Trevor Okafor
• Managing Director
• 02 6140 9375
• 0471 903 216
• wandermereplant@fernmail.example
Nice to have
• Nice to have a picture of machinery or part of machinery in the business card design. We would also like to incorporate our business activities which are: demolition, earthmoving, road works and cartage. It would also be highly desirable if it included a list of our machinery: Watercarts, Rollers, Excavator, Bobcat, Truck & Dog. we are open to the possibility of either single sided or double sided designs
Should not have
• should not have too many colours or detract from the main information. should not be too busy.

```html
<!DOCTYPE html>
<html lang="en">
<head>
<meta charset="utf-8">
<title>Wandermere Plant — Business Card</title>
<link rel="stylesheet" href="https://fonts.googleapis.com/css2?family=Alfa+Slab+One&family=Libre+Baskerville:wght@700&family=Arimo:wght@400&display=swap">
<style>
  :root {
    --yellow: #ebf02d;
    --black: #000000;
    --white: #ffffff;
    --backdrop: #e4e4e4;
    --slab: "Alfa Slab One", Georgia, serif;
    --serif: "Libre Baskerville", Georgia, serif;
    --sans: "Arimo", Arial, sans-serif;
  }
  * { margin: 0; padding: 0; box-sizing: border-box; }
  html, body {
    width: 1189px; height: 1200px; overflow: hidden;
    background: var(--backdrop);
  }
  .card {
    position: absolute; left: 140px; width: 917px; height: 524px;
    background: var(--white); overflow: hidden;
  }
  .card--front { top: 45px; }
  .card--back { top: 650px; }

  .brand { position: absolute; display: flex; align-items: center; }
  .brand__dot { border-radius: 50%; background: var(--yellow); flex: none; }
  .brand__name {
    font-family: var(--slab); font-weight: 400; color: var(--black);
    line-height: 1.05; white-space: nowrap;
  }

  .card--front .brand { left: 40px; top: 114px; gap: 16px; }
  .card--front .brand__dot { width: 104px; height: 104px; }
  .card--front .brand__name { font-size: 30px; }

  .services { position: absolute; font-family: var(--slab); color: var(--black); text-transform: uppercase; white-space: nowrap; }
  .services__main { display: block; }
  .services__sub { display: block; }

  .card--front .services { left: 436px; top: 104px; }
  .card--front .services__main { font-size: 57px; letter-spacing: 0.5px; line-height: 66px; }
  .card--front .services__sub { font-size: 35px; letter-spacing: 0.5px; line-height: 46px; margin-top: 2px; padding-left: 6px; }

  .accent-stripe { position: absolute; left: 0; top: 315px; width: 100%; height: 15px; background: var(--yellow); }
  .contact-band { position: absolute; left: 0; top: 330px; width: 100%; height: 194px; background: var(--black); color: var(--white); }

  .person { position: absolute; left: 30px; top: 46px; font-family: var(--serif); font-weight: 700; white-space: nowrap; }
  .person__name { font-size: 44px; line-height: 56px; display: block; }
  .person__role { font-size: 28px; line-height: 34px; display: block; }

  .divider { position: absolute; left: 410px; top: 28px; width: 2px; height: 134px; background: var(--white); }

  .contact-list { position: absolute; left: 426px; top: 38px; list-style: none; font-family: var(--sans); }
  .contact-list li { display: flex; align-items: center; height: 42px; font-size: 23px; white-space: nowrap; }
  .contact-list svg { width: 22px; height: 22px; margin-right: 22px; flex: none; }

  .card--back .brand { left: 50%; top: 110px; transform: translateX(-50%); gap: 26px; }
  .card--back .brand__dot { width: 160px; height: 160px; }
  .card--back .brand__name { font-size: 58px; }
  .card--back .services { left: 0; width: 100%; top: 325px; text-align: center; }
  .card--back .services__main { font-size: 66px; letter-spacing: 1px; line-height: 80px; }
  .card--back .services__sub { font-size: 42px; letter-spacing: 1px; line-height: 56px; margin-top: 8px; }
</style>
</head>
<body>

<section class="card card--front">
  <div class="brand">
    <span class="brand__dot"></span>
    <span class="brand__name">Wandermere<br>Plant</span>
  </div>
  <p class="services">
    <span class="services__main">Watercarts</span>
    <span class="services__sub">Rollers • Cartage</span>
  </p>
  <div class="accent-stripe"></div>
  <div class="contact-band">
    <p class="person">
      <span class="person__name">Trevor Okafor</span>
      <span class="person__role">Managing Director</span>
    </p>
    <span class="divider"></span>
    <ul class="contact-list">
      <li>
        <svg viewBox="0 0 22 22" aria-hidden="true"><rect width="22" height="22" fill="#fff"/><path d="M4 8c4-4 10-4 14 0l-2 2-2-1v-2H8v2l-2 1z M6 11h10v6H6z" fill="#000"/></svg>
        02 6140 9375
      </li>
      <li>
        <svg viewBox="0 0 22 22" aria-hidden="true"><rect width="22" height="22" fill="#fff"/><path d="M7 4l3 4-2 2c1 2 2 3 4 4l2-2 4 3-2 3c-6 0-12-6-12-12z" fill="#000"/></svg>
        0471 903 216
      </li>
      <li>
        <svg viewBox="0 0 22 22" aria-hidden="true"><rect width="22" height="22" fill="#fff"/><rect x="3" y="6" width="16" height="11" fill="none" stroke="#000" stroke-width="1.6"/><path d="M3 6l8 6 8-6" fill="none" stroke="#000" stroke-width="1.6"/></svg>
        wandermereplant@fernmail.example
      </li>
    </ul>
  </div>
</section>

<section class="card card--back">
  <div class="brand">
    <span class="brand__dot"></span>
    <span class="brand__name">Wandermere<br>Plant</span>
  </div>
  <p class="services">
    <span class="services__main">Watercarts</span>
    <span class="services__sub">Rollers • Cartage</span>
  </p>
</section>

</body>
</html>
```